Need simple and modern looking business card with all my information on one side and logo on the other side
Info :
Company name - VELMAR CONSTRUCTION LLC
Company addres- 418 harbor 87th. Dunmoor park ny 10352
Email- velmarllc@tridomail.Com
Company phone number 555-318-6094
Cell number- 555-742-0583
Web site - velmarllc.Com
My name Gerald tomasino

Target Market(s)

Construction , home improvement, remodeling

Industry/Entity Type

Construction

Contact Information for Business Card

It has to be moder but at the same time simple

Font styles to use
Sans Serif

Colors
0255a3
ffffff
000000
f78f20
b1b1b1
9d9d9d
1b1b1b
33a6d7
ec1f27

Requirements
Must have
• My logo on one side maybe with a some kind of background on the other side all my information
Nice to have
• Some kind of background pictures provided by you .PLEASE HAVE ACCOUNT WITH PIXELVAULT WILL NOT PAY ANY EXTRA FEES .
Should not have
• Any kind of hamer, nails,screws, helmets itp. Please do not copy the other designs come up with something new.

```html
<!DOCTYPE html>
<html lang="en">
<head>
<meta charset="utf-8">
<title>Velmar Construction LLC – Business Card</title>
<link href="https://fonts.googleapis.com/css2?family=Open+Sans:wght@400;600;700&display=swap" rel="stylesheet">
<style>
  :root{
    --blue:#0255a3;
    --bar-blue:#1f6fb8;
    --orange:#f78f20;
    --red:#ec1f27;
    --ink:#1b1b1b;
    --black:#000000;
    --white:#ffffff;
    --stage:#ececec;
    --photo-light:#f3f5f7;
    --photo-mid:#d9dde2;
  }
  *{margin:0;padding:0;box-sizing:border-box}
  html,body{width:1200px;height:1000px;overflow:hidden}
  body{background:var(--stage);position:relative;font-family:"Open Sans",Arial,sans-serif;color:var(--ink)}
  .card{position:absolute;left:265px;width:666px;height:396px;background:var(--white);box-shadow:0 3px 10px rgba(0,0,0,.18);overflow:hidden}
  .card--front{top:73px}
  .card--back{top:533px}

  .brand-name{font-family:"Open Sans",Arial,sans-serif;font-weight:700;color:var(--black);text-align:center;line-height:1.1;letter-spacing:.5px}
  .card--front .brand-name{position:absolute;left:30px;top:112px;width:280px;font-size:27px}

  .contact{position:absolute;left:407px;top:64px;width:250px}
  .contact__name{font-size:20px;font-weight:600;color:var(--orange);line-height:1.2}
  .contact__title{font-size:16px;line-height:1.3}
  .contact__rule{width:74px;height:2px;background:var(--red);margin:20px 0 18px}
  .contact__company{font-size:16px;font-weight:700;line-height:1.35}
  .contact__address{font-size:16px;line-height:1.35}
  .contact__list{list-style:none;margin-top:0}
  .contact__item{display:flex;align-items:center;font-size:16px;line-height:24.5px}
  .contact__icon{width:14px;height:14px;margin-right:8px;flex:none}

  .bands{position:absolute;left:0;bottom:0;width:100%;height:10px}
  .band{position:absolute;top:0;height:10px}
  .band--a{left:0;width:383px;background:var(--bar-blue)}
  .band--b{left:388px;width:220px;background:var(--orange)}
  .band--c{left:612px;width:54px;background:var(--bar-blue)}

  .back-photo{position:absolute;inset:0;background:linear-gradient(160deg,var(--photo-mid) 0%,var(--photo-light) 45%,var(--white) 70%,var(--photo-mid) 100%)}
  .card--back .brand-name{position:absolute;left:140px;top:170px;width:390px;font-size:38px}
</style>
</head>
<body>
  <section class="card card--front">
    <div class="brand-name">VELMAR CONSTRUCTION LLC</div>

    <div class="contact">
      <p class="contact__name">Gerald tomasino</p>
      <p class="contact__title">President</p>
      <div class="contact__rule"></div>
      <p class="contact__company">Velmar Construction LLC</p>
      <p class="contact__address">418 Harbor 87th St,<br>Dunmoor Park, NY 10352</p>
      <div class="contact__rule"></div>
      <ul class="contact__list">
        <li class="contact__item">
          <svg class="contact__icon" viewBox="0 0 14 14"><rect x="3.5" y="1" width="7" height="12" rx="1.2" fill="none" stroke="#f78f20" stroke-width="1.4"/><rect x="5" y="3" width="4" height="5" fill="#f78f20"/></svg>
          555-742-0583
        </li>
        <li class="contact__item">
          <svg class="contact__icon" viewBox="0 0 14 14"><path d="M1 5c0-2 2-3 6-3s6 1 6 3v1h-3V4.5H4V6H1z" fill="#f78f20"/><path d="M3 7h8l1.5 5h-11z" fill="#f78f20"/></svg>
          555-318-6094
        </li>
        <li class="contact__item">
          <svg class="contact__icon" viewBox="0 0 14 14"><rect x="1" y="3" width="12" height="8" fill="#f78f20"/><path d="M1 3l6 4.5L13 3" fill="none" stroke="#fff" stroke-width="1.1"/></svg>
          velmarllc@tridomail.com
        </li>
        <li class="contact__item">
          <svg class="contact__icon" viewBox="0 0 14 14"><circle cx="7" cy="7" r="5.8" fill="none" stroke="#f78f20" stroke-width="1.4"/><path d="M1.5 7h11M7 1.2c-2.5 3-2.5 8.6 0 11.6M7 1.2c2.5 3 2.5 8.6 0 11.6" fill="none" stroke="#f78f20" stroke-width="1"/></svg>
          www.velmarllc.com
        </li>
      </ul>
    </div>

    <div class="bands">
      <span class="band band--a"></span>
      <span class="band band--b"></span>
      <span class="band band--c"></span>
    </div>
  </section>

  <section class="card card--back">
    <div class="back-photo" role="img" aria-label="Faded photo of a building under construction with scaffolding, a tower crane and a worker in a high-visibility jacket"></div>
    <div class="brand-name">VELMAR CONSTRUCTION LLC</div>
  </section>
</body>
</html>
```